OPRU Membership Certificate

We are launching an online membership for www.opru-members.example

When someone joins they will receive a membership certificate that outlines their name, membership number, membership status, date of membership

```html
<!DOCTYPE html>
<html lang="en">
<head>
<meta charset="UTF-8">
<title>OPRU Membership Certificate</title>
<link href="https://fonts.googleapis.com/css2?family=Manrope:wght@400;500;700;800&display=swap" rel="stylesheet">
<style>
  :root {
    --navy: #27306a;
    --navy-text: #2d3575;
    --yellow: #f0d048;
    --paper: #ffffff;
    --rule: #7d82a8;
  }
  html, body {
    margin: 0;
    padding: 0;
    overflow: hidden;
    background: var(--paper);
  }
  .certificate {
    position: relative;
    width: 848px;
    height: 1200px;
    overflow: hidden;
    background: var(--paper);
    font-family: "Manrope", sans-serif;
    color: var(--navy);
  }
  .sweep {
    position: absolute;
    inset: 0;
    width: 848px;
    height: 1200px;
  }
  .title {
    position: absolute;
    left: 73px;
    top: 78px;
    margin: 0;
    font-weight: 700;
    font-size: 95px;
    line-height: 1;
    letter-spacing: -1px;
  }
  .subtitle {
    position: absolute;
    left: 75px;
    top: 178px;
    margin: 0;
    font-weight: 700;
    font-size: 52px;
    line-height: 1;
    letter-spacing: -0.5px;
  }
  .presented {
    position: absolute;
    left: 71px;
    top: 334px;
    margin: 0;
    font-weight: 600;
    font-size: 36px;
    line-height: 1;
    letter-spacing: 1px;
  }
  .field-line {
    position: absolute;
    height: 0;
    border-top: 2px dotted var(--rule);
  }
  .field-line--name { left: 69px; top: 482px; width: 593px; }
  .field-line--number { left: 69px; top: 709px; width: 320px; }
  .field-line--start { left: 69px; top: 820px; width: 320px; }
  .field-line--date { left: 73px; top: 1007px; width: 305px; }
  .statement {
    position: absolute;
    left: 71px;
    top: 527px;
    margin: 0;
    font-weight: 400;
    font-size: 22.5px;
    line-height: 40px;
    color: var(--navy-text);
  }
  .field-label {
    position: absolute;
    margin: 0;
    font-weight: 400;
    font-size: 22.5px;
    line-height: 1;
    color: var(--navy-text);
  }
  .field-label--start { left: 71px; top: 733px; }
  .field-label--date { left: 76px; top: 1024px; }
  .org-badge {
    position: absolute;
    left: 585px;
    top: 1071px;
    width: 234px;
    height: 87px;
    box-sizing: border-box;
    border: 1.5px solid var(--paper);
    background: var(--navy);
    display: flex;
    align-items: center;
  }
  .org-badge__square {
    width: 82px;
    height: 84px;
    background: var(--paper);
    flex: none;
  }
  .org-badge__name {
    margin: 0 0 0 12px;
    font-weight: 500;
    font-size: 14.5px;
    line-height: 17.5px;
    color: var(--paper);
    text-transform: uppercase;
  }
</style>
</head>
<body>
  <main class="certificate">
    <svg class="sweep" viewBox="0 0 848 1200" aria-hidden="true">
      <path fill="var(--navy)" d="M778 0 H848 V1200 H236 C520 1060 778 790 778 424 Z"/>
      <path fill="var(--yellow)" d="M805 0 H848 V340 C848 770 620 990 349 1200 H290 C570 1010 805 770 805 424 Z"/>
    </svg>

    <h1 class="title">CERTIFICATE</h1>
    <h2 class="subtitle">OF MEMBERSHIP</h2>

    <p class="presented">PRESENTED TO</p>
    <div class="field-line field-line--name"></div>

    <p class="statement">
      This is to certify that person stated above was admitted<br>
      as an official member of Online Professional Research<br>
      Union, with membership no:
    </p>
    <div class="field-line field-line--number"></div>

    <p class="field-label field-label--start">started from</p>
    <div class="field-line field-line--start"></div>

    <div class="field-line field-line--date"></div>
    <p class="field-label field-label--date">Date</p>

    <div class="org-badge">
      <div class="org-badge__square"></div>
      <p class="org-badge__name">Online<br>Professional<br>Research<br>Union</p>
    </div>
  </main>
</body>
</html>
```